Business Card, Stationary with Shark Logo for Personal Injury Lawyer

I need business cards and stationery with a shark logo for my Personal Injury Law Practice. Has to have this written on it:
Martin K. Holloway
Injury Lawyer
The Copperfield Building
718 Wexley Street
Eastbrook, Rhode Island 02990
401-555-0172
Martinholloway.example

Contact Information for Business Card

Martin K. Holloway, Injury Lawyer, address, 401-555-0172, martinholloway.example

```html
<!DOCTYPE html>
<html lang="en">
<head>
<meta charset="utf-8">
<title>Martin K. Holloway – Stationery</title>
<link href="https://fonts.googleapis.com/css2?family=Montserrat:wght@500;700;800&family=Open+Sans:wght@400;600&display=swap" rel="stylesheet">
<style>
  :root{
    --navy:#262262;
    --gold-light:#f9ed8e;
    --gold:#e6be58;
    --gold-deep:#d49a3a;
    --ink:#5a5a66;
    --line:#9a9aa6;
    --paper:#ffffff;
    --stage:#e9eaed;
    --stage-top:#f3f4f6;
  }
  *{box-sizing:border-box;margin:0;padding:0}
  html,body{width:1200px;height:2328px;overflow:hidden}
  body{position:relative;background:var(--stage);font-family:"Open Sans",Arial,sans-serif;color:var(--ink)}

  .brand{font-family:"Montserrat",Arial,sans-serif;font-weight:800;text-transform:uppercase;line-height:.95;letter-spacing:-.5px}

  .masthead{position:absolute;left:0;top:0;width:1200px;height:249px;
    background:radial-gradient(ellipse at 50% 40%,#fafafa 0%,#e4e5e8 70%,#d6d7db 100%);
    display:flex;align-items:center;justify-content:center}
  .masthead .brand{color:var(--navy);font-size:58px;text-align:center}
  .rule{position:absolute;left:0;width:1200px;height:4px;background:var(--navy)}

  .preview{position:absolute;left:0;top:253px;width:1200px;height:610px;background:var(--stage-top)}

  .card{position:absolute;width:521px;height:312px;overflow:hidden;box-shadow:0 6px 14px rgba(0,0,0,.22)}
  .card--front{background:var(--navy);display:flex;align-items:center;justify-content:center}
  .card--front .brand{color:var(--gold);font-size:36px;text-align:center}
  .card--back{background:linear-gradient(115deg,var(--gold-light) 0%,var(--gold) 45%,var(--gold-deep) 100%)}
  .ornament{position:absolute}
  .card--front .ornament{background:radial-gradient(circle at var(--at),rgba(226,170,70,.55) 0%,rgba(226,170,70,.15) 45%,transparent 70%)}
  .card--back .ornament{background:radial-gradient(circle at var(--at),rgba(180,110,25,.45) 0%,rgba(180,110,25,.12) 45%,transparent 70%)}
  .ornament--tr{right:0;top:0;width:230px;height:230px;--at:100% 0%}
  .ornament--bl{left:0;bottom:0;width:230px;height:210px;--at:0% 100%}

  .card-mark{position:absolute;left:88px;top:108px;width:150px;color:var(--navy);font-size:27px;text-align:center}
  .card-divider{position:absolute;left:262px;top:108px;width:1px;height:88px;background:var(--navy)}
  .card-info{position:absolute;left:274px;top:104px;color:var(--navy)}
  .card-name{font-family:"Montserrat",Arial,sans-serif;font-weight:700;font-size:15px;text-transform:uppercase}
  .card-role{font-size:12px;margin-top:2px}
  .card-contact{font-size:12.5px;margin-top:12px;line-height:19px}
  .contact-row{display:flex;align-items:center;gap:5px}
  .contact-row svg{width:10px;height:10px;flex:none}
  .card-address{position:absolute;left:0;width:521px;top:212px;text-align:center;color:var(--navy);font-size:12.5px;line-height:15px}

  .mini{transform:scale(.86);transform-origin:top left}

  .letterhead{position:absolute;left:623px;top:919px;width:526px;height:737px;background:var(--paper);overflow:hidden;box-shadow:0 6px 14px rgba(0,0,0,.18)}
  .small-mark{position:absolute;color:var(--navy);font-size:13px}
  .letterhead .small-mark{left:24px;top:48px;width:92px}
  .letterhead-rule{position:absolute;left:122px;top:82px;width:275px;height:1px;background:var(--line)}
  .sender{position:absolute;font-size:7.5px;line-height:9.5px;color:var(--ink)}
  .letterhead .sender{left:400px;top:59px}
  .letter-title{position:absolute;left:32px;top:150px;font-family:"Montserrat",Arial,sans-serif;font-weight:700;font-size:9px;color:var(--navy)}
  .letter-body{position:absolute;left:32px;top:168px;width:462px;font-size:7px;line-height:10.2px;text-align:justify;color:#7a7a84}
  .letter-body p{margin-bottom:17px}
  .signature{position:absolute;left:32px;top:556px;width:180px;height:45px;background:linear-gradient(90deg,#e4e4ea,#f4f4f7)}
  .letter-footer{position:absolute;left:32px;top:680px;padding-left:5px;border-left:1px solid var(--navy);font-size:7.5px;line-height:12px;color:var(--ink)}
  .letter-footer svg{width:7px;height:7px}
  .wave{position:absolute;right:0;bottom:0;width:185px;height:215px;border-top-left-radius:100% 60%;
    background:linear-gradient(135deg,rgba(38,34,98,.08) 0%,rgba(38,34,98,.45) 40%,var(--navy) 75%)}

  .envelope{position:absolute;top:1703px;width:535px;height:269px;background:var(--paper);overflow:hidden;box-shadow:0 6px 14px rgba(0,0,0,.18)}
  .envelope--front{left:50px}
  .envelope--front .small-mark{left:26px;top:30px;width:96px;font-size:13.5px}
  .envelope--front .sender{left:26px;top:203px}
  .envelope--front .wave{width:200px;height:245px}
  .envelope--back{left:613px}
  .flap{position:absolute;left:0;top:0;width:535px;height:75px;background:var(--navy);border-radius:0 0 40px 40px;display:flex;align-items:center;justify-content:center}
  .flap .brand{color:#fff;font-size:13.5px;text-align:center}
</style>
</head>
<body>

<header class="masthead">
  <div class="brand">Martin K.<br>Holloway</div>
</header>
<div class="rule" style="top:249px"></div>

<section class="preview">
  <div class="card card--front mini" style="left:78px;top:170px">
    <div class="ornament ornament--tr" role="img" aria-label="Gold flourish ornament"></div>
    <div class="ornament ornament--bl" role="img" aria-label="Gold flourish ornament"></div>
    <div class="brand">Martin K.<br>Holloway</div>
  </div>
  <div class="card card--back mini" style="left:674px;top:170px">
    <div class="ornament ornament--tr" role="img" aria-label="Gold flourish ornament"></div>
    <div class="ornament ornament--bl" role="img" aria-label="Gold flourish ornament"></div>
    <div class="card-mark brand">Martin K.<br>Holloway</div>
    <div class="card-divider"></div>
    <div class="card-info">
      <div class="card-name">Martin K. Holloway</div>
      <div class="card-role">Injury Lawyer</div>
      <div class="card-contact">
        <div class="contact-row"><svg viewBox="0 0 10 10"><circle cx="5" cy="5" r="5" fill="#262262"/><path d="M3.2 2.6l1 .9-.5.8a4 4 0 0 0 2 2l.8-.5.9 1-.7.7C5 7.4 2.6 5 2.5 3.3z" fill="#e6be58"/></svg>401-555-0172</div>
        <div class="contact-row"><svg viewBox="0 0 10 10"><circle cx="5" cy="5" r="4.4" fill="none" stroke="#262262" stroke-width="1.2"/><path d="M1 5h8M5 .8c-2 2.5-2 5.9 0 8.4M5 .8c2 2.5 2 5.9 0 8.4" fill="none" stroke="#262262" stroke-width=".8"/></svg>www.martinholloway.example</div>
      </div>
    </div>
    <div class="card-address">The Copperfield Building 718 Wexley Street<br>Eastbrook, Rhode Island 02990</div>
  </div>
</section>
<div class="rule" style="top:863px"></div>

<div class="card card--front" style="left:50px;top:919px">
  <div class="ornament ornament--tr" role="img" aria-label="Gold flourish ornament"></div>
  <div class="ornament ornament--bl" role="img" aria-label="Gold flourish ornament"></div>
  <div class="brand">Martin K.<br>Holloway</div>
</div>

<div class="card card--back" style="left:50px;top:1340px">
  <div class="ornament ornament--tr" role="img" aria-label="Gold flourish ornament"></div>
  <div class="ornament ornament--bl" role="img" aria-label="Gold flourish ornament"></div>
  <div class="card-mark brand">Martin K.<br>Holloway</div>
  <div class="card-divider"></div>
  <div class="card-info">
    <div class="card-name">Martin K. Holloway</div>
    <div class="card-role">Injury Lawyer</div>
    <div class="card-contact">
      <div class="contact-row"><svg viewBox="0 0 10 10"><circle cx="5" cy="5" r="5" fill="#262262"/><path d="M3.2 2.6l1 .9-.5.8a4 4 0 0 0 2 2l.8-.5.9 1-.7.7C5 7.4 2.6 5 2.5 3.3z" fill="#e6be58"/></svg>401-555-0172</div>
      <div class="contact-row"><svg viewBox="0 0 10 10"><circle cx="5" cy="5" r="4.4" fill="none" stroke="#262262" stroke-width="1.2"/><path d="M1 5h8M5 .8c-2 2.5-2 5.9 0 8.4M5 .8c2 2.5 2 5.9 0 8.4" fill="none" stroke="#262262" stroke-width=".8"/></svg>www.martinholloway.example</div>
    </div>
  </div>
  <div class="card-address">The Copperfield Building 718 Wexley Street<br>Eastbrook, Rhode Island 02990</div>
</div>

<article class="letterhead">
  <div class="small-mark brand">Martin K.<br>Holloway</div>
  <div class="letterhead-rule"></div>
  <div class="sender">The Copperfield Building<br>718 Wexley Street<br>Eastbrook, Rhode Island 02990</div>
  <h2 class="letter-title">LOREM IPSUM</h2>
  <div class="letter-body">
    <p>Thank you for contacting our office about your recent accident. We have reviewed the details you shared with us and believe you may have a strong claim for compensation. Our team will now gather medical records, witness statements, photographs and insurance documents so that your case is prepared carefully and presented with confidence. We will also confirm the deadlines that apply to your claim and make sure that every required notice is filed on time, so that nothing is missed while you focus on getting better.</p>
    <p>During the first weeks we will contact the other parties and their insurers on your behalf. You should not sign any release or accept any payment before speaking with us. Please keep every receipt, bill and letter you receive, and write down how your injuries affect your work, your sleep and your daily routine. These notes often matter a great deal when we explain the full cost of an injury. We will also arrange any further medical reports that are needed and keep you informed of each step. If your situation changes, or if you receive a call from an adjuster, let us know right away so we can respond promptly and protect your interests. In many cases the insurer will ask for a recorded statement early on. Politely decline and refer them to our office, since a short conversation can be used later to question the extent of your injuries. We will also review your own policies to see whether additional coverage applies, including medical payments, lost wage benefits or protection against drivers who carry little or no insurance. Where a vehicle, a property or a product played a part, we may send an investigator to inspect the scene, take measurements and preserve evidence before it is repaired or lost. Your treatment comes first, so please attend every appointment and follow the advice of your doctors, because gaps in care are often raised by the other side as a reason to reduce an offer.</p>
    <p>Most claims are settled without a trial, but we prepare every file as if it will be heard in court. That approach gives us a stronger position in negotiation and helps us reach a fair result sooner. Once your treatment is complete, or once your doctors can describe your long term outlook, we will prepare a detailed demand that sets out your medical costs, lost income, future care and the impact the injury has had on your life. We will review any offer with you in plain terms and never accept one without your approval. If the insurer refuses to make a reasonable offer, we will discuss filing a lawsuit and explain what each stage of the process involves, from written questions and depositions to mediation and trial. Throughout the case you will have a direct contact at our office who can answer questions, share updates and schedule meetings at a time that suits you. Our fees are only collected if we recover compensation for you.</p>
    <p>Please call our office with any questions at all, or stop by during business hours if you would prefer to talk in person. We look forward to working with you and to helping you move ahead with your recovery. Thank you again for placing your trust in our firm.</p>
  </div>
  <div class="signature" role="img" aria-label="Handwritten signature"></div>
  <div class="letter-footer">
    <div class="contact-row"><svg viewBox="0 0 10 10"><circle cx="5" cy="5" r="5" fill="#262262"/></svg>401-555-0172</div>
    <div class="contact-row"><svg viewBox="0 0 10 10"><circle cx="5" cy="5" r="5" fill="#262262"/></svg>www.martinholloway.example</div>
  </div>
  <div class="wave" role="img" aria-label="Navy flourish ornament"></div>
</article>

<div class="envelope envelope--front">
  <div class="small-mark brand">Martin K.<br>Holloway</div>
  <div class="sender">The Copperfield Building<br>718 Wexley Street<br>Eastbrook, Rhode Island 02990</div>
  <div class="wave" role="img" aria-label="Navy flourish ornament"></div>
</div>

<div class="envelope envelope--back">
  <div class="flap"><div class="brand">Martin K.<br>Holloway</div></div>
</div>

</body>
</html>
```